We are wanting Flagpole Technical Spec sheets custom to our company of which certain fields are editable per project to submit to architects/engineers in pdf format.
Examples 1 and 2 attached are good basic oneline details, however not very fancy and limited in details on bottom right are specific to one flagpole.
Examples 3 and 4 have better graphics however limited in details on bottom right are specific to one flagpole.
we would like a two page spec sheet. 1st page removes specifications and the second page would have flagpole specifications similar to Examples 5 and 6
page 1 editable fields would be; customer and/or job name, date, part number, notes
page 2 would like to be able to highlight, make bold, have stand out the entire line of the specific flagpole catalog number so as to show it matches the catalog number on page 1
the final design will need to include our logo attached as well as contact information at the footer as seen on examples 1 and 2

```html
<!DOCTYPE html>
<html lang="en">
<head>
<meta charset="utf-8">
<title>Flagpole Technical Specification</title>
<link href="https://fonts.googleapis.com/css2?family=Manrope:wght@400;500;600;700;800&display=swap" rel="stylesheet">
<style>
:root{
  --bg:#d6d6d6;
  --paper:#ffffff;
  --cream:#f5f2e6;
  --navy:#13213f;
  --gold:#b89a5a;
  --gold-soft:#e9e0c6;
  --ink:#1d1d1f;
  --muted:#555a63;
  --line:#d9d4c4;
  --drawing:#f3f3f1;
}
*{box-sizing:border-box;margin:0;padding:0}
html,body{width:1200px;height:1031px;overflow:hidden;background:var(--bg);font-family:'Manrope',sans-serif;color:var(--ink)}
.page{position:absolute;top:140px;width:531px;height:752px;background:var(--paper)}
.page--drawing{left:49px}
.page--catalog{left:619px}
.header{position:absolute;left:0;top:0;width:100%;height:110px;background:var(--cream)}
.brand{position:absolute;left:30px;top:24px;width:92px;text-align:center;color:var(--navy);font-weight:800;line-height:1.05}
.brand-dot{display:block;width:14px;height:14px;border-radius:50%;background:var(--navy);margin:0 auto 6px}
.brand-name{font-size:15px;letter-spacing:.5px}
.brand-sub{font-size:7.5px;margin-top:3px}
.title{position:absolute;left:145px;top:31px;font-size:15px;font-weight:800;color:var(--navy);letter-spacing:.1px}
.subtitle{position:absolute;left:145px;top:53px;font-size:7.3px;color:var(--muted)}
.field{position:absolute;top:71px}
.field label{display:block;font-size:5.3px;font-weight:600;color:var(--ink);margin-bottom:3px;letter-spacing:.1px}
.field .input{height:19px;background:#fff;border:1px solid #e4dfcf;border-radius:2px}
.section-label{position:absolute;font-size:7.3px;font-weight:500}
.notes-box{position:absolute;left:28px;top:132px;width:471px;height:66px;border:1px solid #c9b985;border-radius:4px}
.detail-label{position:absolute;left:25px;top:211px;font-size:7px;font-weight:700;color:var(--gold)}
.drawing{position:absolute;left:14px;top:226px;width:365px;height:458px;background:var(--drawing)}
.card{position:absolute;left:385px;width:123px;height:69px;border:1px solid #c9b985;border-radius:5px;background:#fff}
.card-title{position:absolute;left:5px;top:6px;font-size:4.6px;font-weight:700;display:flex;align-items:center;gap:2px}
.card-num{width:6px;height:6px;border-radius:50%;background:var(--gold);color:#fff;font-size:4px;display:flex;align-items:center;justify-content:center}
.card-photo{position:absolute;left:30px;top:15px;width:62px;height:48px;border-radius:4px}
.photo-ball{background:radial-gradient(circle at 45% 40%,#f2c44c,#c9921b 70%,#fff 72%)}
.photo-truck{background:linear-gradient(#8b8d90,#5a5c60)}
.photo-hood{background:linear-gradient(90deg,#8e9194,#e4e6e8 50%,#8e9194)}
.photo-snap{background:linear-gradient(#e6e7e8,#b8babc)}
.photo-weight{background:radial-gradient(circle at 50% 55%,#1a1a1a 45%,#fff 47%)}
.card-add{position:absolute;left:47px;top:27px}
.note{position:absolute;left:29px;top:706px;font-size:5.4px;color:var(--ink)}
.footer-rule{position:absolute;left:29px;right:28px;top:718px;border-top:1px solid var(--gold)}
.footer-name{position:absolute;left:29px;top:723px;font-size:7.4px;font-weight:700}
.footer-contact{position:absolute;right:28px;top:723px;font-size:7.4px;text-align:right}
.footer-page{position:absolute;right:28px;top:734px;font-size:5px;font-weight:700;color:var(--gold)}
.spec-table{position:absolute;left:23px;top:124px;width:485px;border-collapse:collapse;table-layout:fixed;font-size:4.8px}
.spec-table th{background:var(--navy);color:#fff;font-weight:700;font-size:4.6px;line-height:1.35;border-right:1px solid #2b3a5c;padding:0 1px}
.spec-table thead tr{height:21.5px}
.spec-table td{text-align:center;height:12.15px;border-bottom:1px solid #eeeae0;padding:0}
.spec-table td.ht{background:var(--gold-soft);font-weight:700;border-bottom:1px solid #fff}
.spec-table tr.grp td:not(.ht){border-top:1px solid #e2dccb}
.finish-title{position:absolute;left:0;width:100%;top:650px;text-align:center;font-size:10px;font-weight:800;color:var(--navy)}
.finishes{position:absolute;left:34px;top:674px;width:480px;display:flex;justify-content:space-between}
.finish{display:flex;align-items:flex-start;gap:10px;width:75px}
.swatch{width:16px;height:16px;border-radius:50%;margin-top:3px;flex:none}
.finish b{display:block;font-size:7.8px;font-weight:800}
.finish span{display:block;font-size:7.6px;line-height:1.05;color:#333}
</style>
</head>
<body>

<section class="page page--drawing">
  <header class="header">
    <div class="brand"><span class="brand-dot"></span><div class="brand-name">RIDGELINE</div><div class="brand-sub">Flag &amp; Flagpole</div></div>
    <h1 class="title">FLAGPOLE TECHNICAL SPECIFICATION</h1>
    <p class="subtitle">Project-specific submittal • Commercial groundset flagpole</p>
    <div class="field" style="left:145px;width:146px"><label>CUSTOMER / JOB NAME</label><div class="input"></div></div>
    <div class="field" style="left:300px;width:76px"><label>DATE</label><div class="input"></div></div>
    <div class="field" style="left:384px;width:93px"><label>PART NUMBER</label><div class="input"></div></div>
  </header>

  <p class="section-label" style="left:29px;top:120px">PROJECT NOTES</p>
  <div class="notes-box"></div>

  <p class="detail-label">STANDARD FLAGPOLE / GROUNDSET DETAIL</p>
  <div class="drawing" role="img" aria-label="Technical line drawing of an aluminum internal halyard groundset flagpole with hood, truck, rigging and winch assembly details"></div>

  <div class="card" style="top:219px"><div class="card-title"><span class="card-num">1</span>BALL ORNAMENT</div><div class="card-photo photo-ball" role="img" aria-label="Gold anodized ball ornament"></div></div>
  <div class="card" style="top:297px"><div class="card-title"><span class="card-num">2</span>TRUCK ASSEMBLY</div><div class="card-photo photo-truck" role="img" aria-label="Cast aluminum truck assembly"></div></div>
  <div class="card" style="top:375px"><div class="card-title"><span class="card-num">3</span>HOOD ASSEMBLY</div><div class="card-photo photo-hood" role="img" aria-label="Cast aluminum hood assembly"></div></div>
  <div class="card" style="top:453px"><div class="card-title"><span class="card-num">4</span>SNAPHOOK &amp; CABLE</div><div class="card-photo photo-snap" role="img" aria-label="Stainless steel snaphook and cable"></div></div>
  <div class="card" style="top:532px"><div class="card-title"><span class="card-num">5</span>COUNTERWEIGHT</div><div class="card-photo photo-weight" role="img" aria-label="Black neoprene coated counterweight"></div></div>
  <div class="card" style="top:610px"><div class="card-title"><span class="card-num">6</span>ADDITIONAL ACCESSORY (PLACEHOLDER)</div>
    <svg class="card-add" width="24" height="24" viewBox="0 0 24 24"><circle cx="12" cy="12" r="10.5" fill="none" stroke="#1d1d1f" stroke-width="1"/><path d="M12 4v16M4 12h16" stroke="#1d1d1f" stroke-width="1"/></svg>
  </div>

  <p class="note">Engineering values and wind-speed criteria are presented on Page 2 from the supplied catalog reference.</p>
  <div class="footer-rule"></div>
  <p class="footer-name">RIDGELINE FLAG &amp; FLAGPOLE 140 Cedar Bend Rd • Dripping Oaks, TX 78600</p>
  <p class="footer-contact">512-555-0148 • info@ridgelineflag.com</p>
  <p class="footer-page">FLAGPOLE TECHNICAL SPECIFICATION 1 | 2</p>
</section>

<section class="page page--catalog">
  <header class="header">
    <div class="brand"><span class="brand-dot"></span><div class="brand-name">RIDGELINE</div><div class="brand-sub">Flag &amp; Flagpole</div></div>
    <h1 class="title">COMMERCIAL GROUNDSET FLAGPOLES</h1>
    <div class="field" style="left:144px;width:257px"><label>SELECTED CATALOG NUMBER</label><div class="input"></div></div>
  </header>

  <table class="spec-table">
    <colgroup><col style="width:6.45%"><col style="width:6.93%"><col style="width:9.68%"><col style="width:8.6%"><col style="width:7.89%"><col style="width:7.53%"><col style="width:8.96%"><col style="width:8%"><col style="width:8%"><col style="width:8.72%"><col style="width:11.23%"><col style="width:8.01%"></colgroup>
    <thead>
      <tr><th rowspan="2">MTG<br>HT.</th><th rowspan="2">BUTT.<br>DIA.</th><th rowspan="2">WALL<br>THICKNESS</th><th rowspan="2">POLE<br>SECTIONS</th><th rowspan="2">SET DEPTH</th><th rowspan="2">TOP<br>DIA.</th><th rowspan="2">STD FLAG<br>SIZE</th><th colspan="3">MAX WIND SPEED WITH NYLON FLAG</th><th rowspan="2">CATALOG<br>NUMBER</th><th rowspan="2">SPECIFY<br>FINISH</th></tr>
      <tr><th>85 MPH</th><th>100 MPH</th><th>110 MPH</th></tr>
    </thead>
    <tbody>
      <tr class="grp"><td class="ht" rowspan="2">20′</td><td>6″</td><td>.156″</td><td>1</td><td>2′-0″</td><td>3.5″</td><td>4′ x 6′</td><td>208</td><td>301</td><td>–</td><td>RFP20C61-***</td><td>$</td></tr>
      <tr><td>6″</td><td>.188″</td><td>1</td><td>2′-0″</td><td>3.5″</td><td>4′ x 6′</td><td>229</td><td>328</td><td>–</td><td>RFP20D61-***</td><td>$</td></tr>
      <tr class="grp"><td class="ht" rowspan="2">25′</td><td>6″</td><td>.156″</td><td>1</td><td>2′-6″</td><td>3.5″</td><td>5′ x 8′</td><td>149</td><td>230</td><td>–</td><td>RFP25C61-***</td><td>$</td></tr>
      <tr><td>6″</td><td>.188″</td><td>1</td><td>2′-6″</td><td>3.5″</td><td>5′ x 8′</td><td>168</td><td>253</td><td>–</td><td>RFP25D61-***</td><td>$</td></tr>
      <tr class="grp"><td class="ht" rowspan="4">30′</td><td>6″</td><td>.156″</td><td>1</td><td>3′-0″</td><td>3.5″</td><td>6′ x 10′</td><td>108</td><td>174</td><td>–</td><td>RFP30C61-***</td><td>$</td></tr>
      <tr><td>6″</td><td>.156″</td><td>2</td><td>3′-0″</td><td>3.5″</td><td>6′ x 10′</td><td>108</td><td>174</td><td>–</td><td>RFP30C62-***</td><td>$</td></tr>
      <tr><td>6″</td><td>.188″</td><td>1</td><td>3′-0″</td><td>3.5″</td><td>6′ x 10′</td><td>122</td><td>197</td><td>–</td><td>RFP30D61-***</td><td>$</td></tr>
      <tr><td>6″</td><td>.188″</td><td>2</td><td>3′-0″</td><td>3.5″</td><td>6′ x 10′</td><td>122</td><td>197</td><td>–</td><td>RFP30D62-***</td><td>$</td></tr>
      <tr class="grp"><td class="ht" rowspan="9">35′</td><td>6″</td><td>.156″</td><td>1</td><td>3′-6″</td><td>3.5″</td><td>6′ x 10′</td><td>87</td><td>116</td><td>–</td><td>RFP35C61-***</td><td>$</td></tr>
      <tr><td>6″</td><td>.156″</td><td>2</td><td>3′-6″</td><td>3.5″</td><td>6′ x 10′</td><td>87</td><td>116</td><td>–</td><td>RFP35C62-***</td><td>$</td></tr>
      <tr><td>6″</td><td>.188″</td><td>1</td><td>3′-6″</td><td>3.5″</td><td>6′ x 10′</td><td>97</td><td>145</td><td>–</td><td>RFP35D61-***</td><td>$</td></tr>
      <tr><td>6″</td><td>.188″</td><td>2</td><td>3′-6″</td><td>3.5″</td><td>6′ x 10′</td><td>97</td><td>145</td><td>–</td><td>RFP35D62-***</td><td>$</td></tr>
      <tr><td>7″</td><td>.156″</td><td>1</td><td>3′-6″</td><td>3.5″</td><td>6′ x 10′</td><td>110</td><td>165</td><td>–</td><td>RFP35C71-***</td><td>$</td></tr>
      <tr><td>7″</td><td>.156″</td><td>2</td><td>3′-6″</td><td>3.5″</td><td>6′ x 10′</td><td>110</td><td>165</td><td>–</td><td>RFP35C72-***</td><td>$</td></tr>
      <tr><td>7″</td><td>.188″</td><td>1</td><td>3′-6″</td><td>3.5″</td><td>6′ x 10′</td><td>127</td><td>187</td><td>–</td><td>RFP35D71-***</td><td>$</td></tr>
      <tr><td>7″</td><td>.188″</td><td>2</td><td>3′-6″</td><td>3.5″</td><td>6′ x 10′</td><td>127</td><td>187</td><td>–</td><td>RFP35D72-***</td><td>$</td></tr>
      <tr><td>8″</td><td>.188″</td><td>1</td><td>3′-6″</td><td>4″</td><td>6′ x 10′</td><td>155</td><td>213</td><td>–</td><td>RFP35D81-***</td><td>$</td></tr>
      <tr class="grp"><td class="ht" rowspan="8">40′</td><td>7″</td><td>.156″</td><td>1</td><td>4′-0″</td><td>3.5″</td><td>8′ x 12′</td><td>87</td><td>122</td><td>–</td><td>RFP40C71-***</td><td>$</td></tr>
      <tr><td>7″</td><td>.156″</td><td>2</td><td>4′-0″</td><td>3.5″</td><td>8′ x 12′</td><td>87</td><td>122</td><td>–</td><td>RFP40C72-***</td><td>$</td></tr>
      <tr><td>7″</td><td>.188″</td><td>1</td><td>4′-0″</td><td>3.5″</td><td>8′ x 12′</td><td>98</td><td>147</td><td>–</td><td>RFP40D71-***</td><td>$</td></tr>
      <tr><td>8″</td><td>.156″</td><td>1</td><td>4′-0″</td><td>4″</td><td>8′ x 12′</td><td>107</td><td>157</td><td>–</td><td>RFP40C81-***</td><td>$</td></tr>
      <tr><td>8″</td><td>.156″</td><td>2</td><td>4′-0″</td><td>3.5″</td><td>8′ x 12′</td><td>107</td><td>157</td><td>–</td><td>RFP40C82-***</td><td>$</td></tr>
      <tr><td>8″</td><td>.188″</td><td>1</td><td>4′-0″</td><td>4″</td><td>8′ x 12′</td><td>122</td><td>177</td><td>–</td><td>RFP40D81-***</td><td>$</td></tr>
      <tr><td>8″</td><td>.188″</td><td>2</td><td>4′-0″</td><td>4″</td><td>8′ x 12′</td><td>122</td><td>177</td><td>–</td><td>RFP40D82-***</td><td>$</td></tr>
      <tr><td>10″</td><td>.188″</td><td>2</td><td>4′-0″</td><td>4″</td><td>8′ x 12′</td><td>166</td><td>226</td><td>–</td><td>RFP40D12-***</td><td>$</td></tr>
      <tr class="grp"><td class="ht" rowspan="3">45′</td><td>8″</td><td>.188″</td><td>2</td><td>4′-6″</td><td>3.5″</td><td>8′ x 12′</td><td>102</td><td>144</td><td>–</td><td>RFP45D82-***</td><td>$</td></tr>
      <tr><td>8″</td><td>.250″</td><td>2</td><td>4′-6″</td><td>3.5″</td><td>8′ x 12′</td><td>125</td><td>173</td><td>–</td><td>RFP45F82-***</td><td>$</td></tr>
      <tr><td>10″</td><td>.188″</td><td>2</td><td>4′-6″</td><td>4″</td><td>8′ x 12′</td><td>143</td><td>192</td><td>–</td><td>RFP45D12-***</td><td>$</td></tr>
      <tr class="grp"><td class="ht" rowspan="3">50′</td><td>8″</td><td>.188″</td><td>3</td><td>5′-0″</td><td>3.5″</td><td>10′ x 15′</td><td>83</td><td>117</td><td>–</td><td>RFP50D83-***</td><td>$</td></tr>
      <tr><td>10″</td><td>.188″</td><td>3</td><td>5′-0″</td><td>4″</td><td>10′ x 15′</td><td>118</td><td>164</td><td>–</td><td>RFP50D13-***</td><td>$</td></tr>
      <tr><td>10″</td><td>.250″</td><td>3</td><td>5′-0″</td><td>4″</td><td>10′ x 15′</td><td>140</td><td>191</td><td>–</td><td>RFP50F13-***</td><td>$</td></tr>
      <tr class="grp"><td class="ht">55′</td><td>10″</td><td>.188″</td><td>3</td><td>5′-6″</td><td>4″</td><td>10′ x 15′</td><td>102</td><td>139</td><td>–</td><td>RFP55D13-***</td><td>$</td></tr>
      <tr class="grp"><td class="ht" rowspan="3">60′</td><td>10″</td><td>.188″</td><td>3</td><td>6′-0″</td><td>4″</td><td>12′ x 18′</td><td>86</td><td>118</td><td>–</td><td>RFP60D13-***</td><td>$</td></tr>
      <tr><td>10″</td><td>.250″</td><td>3</td><td>6′-0″</td><td>4″</td><td>12′ x 18′</td><td>104</td><td>143</td><td>–</td><td>RFP60F13-***</td><td>$</td></tr>
      <tr><td>12″</td><td>.250″</td><td>3</td><td>6′-0″</td><td>4″</td><td>12′ x 18′</td><td>137</td><td>187</td><td>–</td><td>RFP60F23-***</td><td>$</td></tr>
      <tr class="grp"><td class="ht">65′</td><td>12″</td><td>.250″</td><td>3</td><td>6′-6″</td><td>4″</td><td>12′ x 18′</td><td>122</td><td>165</td><td>–</td><td>RFP65F23-***</td><td>$</td></tr>
      <tr class="grp"><td class="ht">70′</td><td>12″</td><td>.250″</td><td>3</td><td>7′-0″</td><td>4″</td><td>12′ x 18′</td><td>109</td><td>145</td><td>–</td><td>RFP70F23-***</td><td>$</td></tr>
      <tr class="grp"><td class="ht">75′</td><td>12″</td><td>.375″</td><td>3</td><td>7′-6″</td><td>4″</td><td>12′ x 18′</td><td>126</td><td>161</td><td>–</td><td>RFP75H23-***</td><td>$</td></tr>
      <tr class="grp"><td class="ht">80′</td><td>12″</td><td>.375″</td><td>3</td><td>8′-0″</td><td>4″</td><td>15′ x 25′</td><td>107</td><td>144</td><td>–</td><td>RFP80H23-***</td><td>$</td></tr>
    </tbody>
  </table>

  <h2 class="finish-title">FINISH OPTIONS (SPECIFY FINISH)</h2>
  <div class="finishes">
    <div class="finish"><span class="swatch" style="background:linear-gradient(90deg,#9a9c9f,#eef0f1,#9a9c9f)"></span><div><b>SAT</b><span>Satin<br>Aluminum</span></div></div>
    <div class="finish"><span class="swatch" style="background:linear-gradient(90deg,#d9c48c,#f7ecc8,#d9c48c)"></span><div><b>FSA</b><span>Satin<br>Anodized</span></div></div>
    <div class="finish"><span class="swatch" style="background:radial-gradient(circle at 40% 35%,#555,#0d0d0d 70%)"></span><div><b>BLK</b><span>Black<br>Anodized</span></div></div>
    <div class="finish"><span class="swatch" style="background:linear-gradient(90deg,#9c7a3e,#d8b878,#9c7a3e)"></span><div><b>BRZ</b><span>Bronze<br>Anodized</span></div></div>
    <div class="finish"><span class="swatch" style="background:#fff;border:1px solid #333"></span><div><b>WHT</b><span>White<br>Anodized</span></div></div>
    <div class="finish"><span class="swatch" style="background:conic-gradient(#e53935,#fbc02d,#43a047,#1e88e5,#8e24aa,#e53935)"></span><div><b>CUSTOM</b><span>Custom<br>Color</span></div></div>
  </div>

  <p class="note">Engineering values and wind-speed criteria are presented on Page 2 from the supplied catalog reference.</p>
  <div class="footer-rule"></div>
  <p class="footer-name">RIDGELINE FLAG &amp; FLAGPOLE 140 Cedar Bend Rd • Dripping Oaks, TX 78600</p>
  <p class="footer-contact">512-555-0148 • info@ridgelineflag.com</p>
  <p class="footer-page">FLAGPOLE TECHNICAL SPECIFICATION 1 | 2</p>
</section>

</body>
</html>
```